Velsori Biotechnology needs a professional powerpoint design

We would like to re-design our powerpoint template(as attachment 1), it should be based on our current logo (as attachment 2). We hope the new powerpoint template could be more professional and like a biotechnology company with advanced technology.
Velsori Biotechnology is a contract development and manufacturing organization to provide high quality services to our clients in development, lead-in advanced technology and cGMP manufacturing of biopharmaceuticals from clinical to commercial manufacturing. We offers the advanced technology and services to become the best partner for clients from clinical to commercial manufacturing.
Reason: We would like to extend the deadline for this project so that designers can have more time to prepare, thanks.
Target Market(s)
Velsori Biotechnology is a contract development and manufacturing organization to provide high quality services to our clients in development, lead-in advanced technology and cGMP manufacturing of biopharmaceuticals from clinical to commercial manufacturing.
Velsori primary focus on development and manufacturing of glycoprotein pharmaceuticals against breast cancer, supplies KEP Taiwan with KEP-437 & KEP-438 for global clinical trials and commercialization in the future. Velsori offers the advanced technology and services to become the best partner for clients from clinical to commercial manufacturing.
Industry/Entity Type
Biotechnology
Requirements
Must have
- The new powerpoint design should based on our current logo.
Should not have
- The similar design with current powerpoint style. Please don't refer the design style of our current website http://www.velsori-example.com.tw/ as well, we will re-design it soon.

```html
<!DOCTYPE html>
<html lang="en">
<head>
<meta charset="utf-8">
<title>Velsori Biotechnology – Presentation Template</title>
<link rel="stylesheet" href="https://fonts.googleapis.com/css2?family=Open+Sans:wght@400;600;700&display=swap">
<style>
:root{
  --stage-top:#4d4d4d;
  --stage-bottom:#121212;
  --navy:#0b2f86;
  --blue:#1a4fc4;
  --blue-light:#3f7fe0;
  --ink:#222;
  --muted:#777;
  --magenta:#b0197f;
  --red:#e0243b;
  --green:#4caf50;
  --table-head:#5b8ed6;
  --table-row:#dbe6f5;
  --white:#fff;
}
*{margin:0;padding:0;box-sizing:border-box}
html,body{width:773px;height:1200px;overflow:hidden}
body{
  font-family:"Open Sans",Arial,sans-serif;
  background:linear-gradient(180deg,var(--stage-top) 0%,#2a2a2a 45%,var(--stage-bottom) 100%);
  position:relative;
}
.slide{
  position:absolute;left:219px;width:336px;height:190px;
  background:var(--white);overflow:hidden;
  box-shadow:0 6px 16px rgba(0,0,0,.55);
}
.slide--cover,.slide--closing{background:transparent}
.slide-art{position:absolute;inset:0;
  background:radial-gradient(ellipse at 70% 30%,var(--blue-light) 0%,var(--blue) 40%,var(--navy) 100%)}
.brand{position:absolute;display:flex;align-items:center;gap:5px;font-weight:700;color:var(--white)}
.brand-dot{width:14px;height:14px;border-radius:50%;background:var(--white)}
.slide--cover .brand{left:26px;top:72px;font-size:22px;letter-spacing:1px}
.slide--cover .brand-dot{width:22px;height:22px}
.slide-title{position:absolute;left:14px;top:10px;font-size:14px;font-weight:700;color:var(--ink)}
.footer-band{position:absolute;left:0;bottom:0;width:100%;height:24px}
.footer-brand{position:absolute;right:8px;bottom:26px;display:flex;align-items:center;gap:3px;
  font-size:7px;font-weight:700;color:var(--blue)}
.footer-brand .brand-dot{width:9px;height:9px;background:var(--blue)}
.body-copy{position:absolute;left:14px;top:34px;width:300px;font-size:5.2px;line-height:1.45;color:var(--muted)}
.bullets{position:absolute;left:22px;font-size:6.5px;color:var(--ink);line-height:1.8}
.slide--services .bullets{top:70px;color:var(--muted)}
.slide--finance .bullets{top:50px}
.chart{position:absolute;left:170px;top:30px;width:160px;height:110px}
.plan-grid{position:absolute;left:12px;top:30px;width:150px;height:112px}
.plan-table{position:absolute;left:180px;top:32px;width:140px;border-collapse:collapse;font-size:4.6px;text-align:center}
.plan-table th{background:var(--table-head);color:var(--white);font-weight:600;padding:3px 1px}
.plan-table td{background:var(--table-row);color:var(--ink);padding:3.4px 1px;border-top:1px solid var(--white)}
.closing-info{position:absolute;left:0;right:0;top:136px;text-align:center;color:var(--white);font-size:4.8px;line-height:1.5}
.closing-info strong{font-size:5.4px;font-weight:700}
</style>
</head>
<body>

<section class="slide slide--cover" style="top:39px">
  <div class="slide-art" role="img" aria-label="Blue abstract DNA helix background"></div>
  <div class="brand"><span class="brand-dot"></span>VELSORI</div>
</section>

<section class="slide slide--services" style="top:258px">
  <h2 class="slide-title">Our Services</h2>
  <p class="body-copy">Lorem Ipsum is simply dummy text of the printing and typesetting industry. Lorem Ipsum has been the industry's standard dummy text ever since the 1500s. Lorem Ipsum is simply dummy text of the printing and typesetting industry. Lorem Ipsum has been the industry's standard dummy text ever since the 1500s.</p>
  <ul class="bullets"><li>Sample Text 1</li><li>Sample Text 2</li><li>Sample Text 3</li></ul>
  <div class="footer-brand"><span class="brand-dot"></span>Velsori</div>
  <svg class="footer-band" viewBox="0 0 336 24" preserveAspectRatio="none"><path d="M0 12 Q120 4 336 10 V24 H0Z" fill="var(--blue-light)"/><path d="M0 16 Q150 8 336 15 V24 H0Z" fill="var(--navy)"/></svg>
</section>

<section class="slide slide--finance" style="top:490px">
  <h2 class="slide-title">Financial Plan 2017</h2>
  <ul class="bullets"><li>Table sample 1</li><li>Table sample 1</li><li>Table sample 3</li><li>Table sample 2</li></ul>
  <svg class="chart" viewBox="0 0 160 110" font-family="Open Sans,Arial,sans-serif" font-size="5" fill="#555">
    <g text-anchor="end"><text x="14" y="12">100%</text><text x="14" y="28">80%</text><text x="14" y="44">60%</text><text x="14" y="60">40%</text><text x="14" y="76">20%</text><text x="14" y="92">0%</text></g>
    <g stroke="#ddd" stroke-width=".5"><line x1="17" y1="10" x2="118" y2="10"/><line x1="17" y1="26" x2="118" y2="26"/><line x1="17" y1="42" x2="118" y2="42"/><line x1="17" y1="58" x2="118" y2="58"/><line x1="17" y1="74" x2="118" y2="74"/><line x1="17" y1="90" x2="118" y2="90"/></g>
    <g><rect x="26" y="58" width="16" height="32" fill="var(--blue-light)"/><rect x="26" y="30" width="16" height="28" fill="var(--red)"/><rect x="26" y="10" width="16" height="20" fill="var(--green)"/>
    <rect x="58" y="62" width="16" height="28" fill="var(--blue-light)"/><rect x="58" y="26" width="16" height="36" fill="var(--red)"/><rect x="58" y="10" width="16" height="16" fill="var(--green)"/>
    <rect x="90" y="54" width="16" height="36" fill="var(--blue-light)"/><rect x="90" y="34" width="16" height="20" fill="var(--red)"/><rect x="90" y="10" width="16" height="24" fill="var(--green)"/></g>
    <g text-anchor="end"><text transform="translate(38 94) rotate(-40)">Category 1</text><text transform="translate(70 94) rotate(-40)">Category 2</text><text transform="translate(102 94) rotate(-40)">Category 3</text></g>
    <g><rect x="124" y="34" width="4" height="4" fill="var(--green)"/><text x="130" y="38">Series 3</text><rect x="124" y="48" width="4" height="4" fill="var(--red)"/><text x="130" y="52">Series 2</text><rect x="124" y="62" width="4" height="4" fill="var(--blue-light)"/><text x="130" y="66">Series 1</text></g>
  </svg>
  <div class="footer-brand"><span class="brand-dot"></span>Velsori</div>
  <svg class="footer-band" viewBox="0 0 336 24" preserveAspectRatio="none"><path d="M0 12 Q120 4 336 10 V24 H0Z" fill="var(--blue-light)"/><path d="M0 16 Q150 8 336 15 V24 H0Z" fill="var(--navy)"/></svg>
</section>

<section class="slide slide--planning" style="top:729px">
  <h2 class="slide-title">Project Planning</h2>
  <svg class="plan-grid" viewBox="0 0 150 112" font-family="Open Sans,Arial,sans-serif" font-size="5" text-anchor="middle">
    <rect x="10" y="4" width="64" height="44" fill="var(--white)" stroke="#ccc" stroke-width=".5"/>
    <text x="42" y="28" fill="#555">Strategy</text>
    <rect x="76" y="4" width="64" height="44" fill="var(--navy)"/>
    <text x="108" y="28" fill="var(--white)">Growth</text>
    <rect x="10" y="50" width="64" height="42" fill="var(--magenta)"/>
    <text x="42" y="73" fill="var(--white)">Review</text>
    <rect x="76" y="50" width="64" height="42" fill="var(--blue)"/>
    <text x="108" y="73" fill="var(--white)">Launch</text>
    <rect x="10" y="96" width="130" height="7" fill="var(--red)"/>
    <text x="75" y="101.5" fill="var(--white)" font-size="4.5">Timeline overview 2017</text>
  </svg>
  <table class="plan-table">
    <tr><th>Task</th><th>Start</th><th>End</th><th>Budget</th></tr>
    <tr><td>Phase 1</td><td>Q1</td><td>Q2</td><td>$120K</td></tr>
    <tr><td>Phase 2</td><td>Q2</td><td>Q3</td><td>$180K</td></tr>
    <tr><td>Phase 3</td><td>Q3</td><td>Q4</td><td>$240K</td></tr>
    <tr><td>Phase 4</td><td>Q4</td><td>Q1</td><td>$150K</td></tr>
  </table>
  <div class="footer-brand"><span class="brand-dot"></span>Velsori</div>
  <svg class="footer-band" viewBox="0 0 336 24" preserveAspectRatio="none"><path d="M0 12 Q120 4 336 10 V24 H0Z" fill="var(--blue-light)"/><path d="M0 16 Q150 8 336 15 V24 H0Z" fill="var(--navy)"/></svg>
</section>

<section class="slide slide--closing" style="top:966px">
  <div class="slide-art" role="img" aria-label="Blue abstract DNA helix background"></div>
  <div class="closing-info">
    <strong>Velsori Biotechnology</strong><br>
    No. 8 Sample Road<br>
    http://www.velsori-example.com.tw/
  </div>
</section>

</body>
</html>
```